Red design in a sea of blue ocean

We need a new vehicle wrap that will stand out and will be noticed over all other contractors wraps . Bright coloring easy to ready name, number and services. Attached are some stand out designs to draw insight from.

++Our business card design is also uploaded. Fee free to take inspiration from the card design swapping colors.

Company: Dorvel Power Max +
Services : residential Service, Commercial Service New Construction
Smart Homes, Solar, LED lighting,

Additional Partnered Services :
Hvac, Plumbing, Window Cleaning Christmas alighting, Home and Vacation Rental cleaning, car detailing

Please make designs on

Varden k 240 with a utility shell
Varden corvo high roof
Varden corvo linka

Home owners

Electric Company

• Name, logo, services and phone number

```html
<!DOCTYPE html>
<html lang="en">
<head>
<meta charset="utf-8">
<title>Dorvel Power Max + — Van Wrap</title>
<link href="https://fonts.googleapis.com/css2?family=Montserrat:wght@500;700;800&display=swap" rel="stylesheet">
<style>
  :root{
    --lime-light:#c8e12a;
    --lime:#8dd02c;
    --lime-deep:#6fc232;
    --brand-blue:#0b5fc9;
    --navy-blue:#1d49a8;
    --charcoal:#2a2d33;
    --ink:#1f2328;
    --white:#ffffff;
    --page:#ffffff;
  }
  html,body{margin:0;padding:0;overflow:hidden;}
  body{width:1040px;height:1200px;background:var(--page);font-family:"Montserrat",sans-serif;}
  .wrap-sheet{position:absolute;left:20px;top:380px;width:1000px;height:378px;}
  .headline{font-family:"Montserrat",sans-serif;font-weight:800;font-size:34px;fill:var(--white);letter-spacing:0.3px;}
  .service-label{font-family:"Montserrat",sans-serif;font-weight:500;font-size:15px;fill:var(--ink);text-anchor:middle;}
  .service-ring{fill:none;stroke:var(--ink);stroke-width:2.6;}
  .service-glyph{fill:var(--ink);}
  .phone-pill{fill:var(--navy-blue);}
  .phone-text{font-family:"Montserrat",sans-serif;font-weight:700;font-size:22px;fill:var(--white);}
  .phone-ring{fill:none;stroke:var(--white);stroke-width:2;}
  .brand-name{font-family:"Montserrat",sans-serif;font-weight:700;font-size:20px;fill:var(--brand-blue);}
  .brand-dot{fill:var(--lime-deep);}
</style>
</head>
<body>
<svg class="wrap-sheet" viewBox="70 130 1060 400" xmlns="http://www.w3.org/2000/svg">
  <defs>
    <linearGradient id="limeBody" x1="0" y1="0" x2="1" y2="1">
      <stop offset="0" stop-color="var(--lime)"/>
      <stop offset="1" stop-color="var(--lime-light)"/>
    </linearGradient>
    <linearGradient id="leafArea" x1="0" y1="1" x2="1" y2="0">
      <stop offset="0" stop-color="var(--navy-blue)"/>
      <stop offset="1" stop-color="var(--brand-blue)"/>
    </linearGradient>
    <clipPath id="vanShape">
      <path d="M102,140 Q90,140 90,160 L88,340 L74,346 L78,443 L310,448 Q362,418 416,452 L935,465 Q975,430 1017,463 L1125,463 L1120,420 Q1106,388 1050,372 L985,320 L960,300 L850,226 Q800,190 770,170 Q720,148 650,144 Z"/>
    </clipPath>
  </defs>

  <g class="van-panel" clip-path="url(#vanShape)">
    <rect class="panel-lime" x="60" y="120" width="1080" height="360" fill="url(#limeBody)"/>
    <path class="panel-charcoal" d="M650,138 Q660,320 430,468 L1140,475 L1140,120 Z" fill="var(--charcoal)"/>
    <g class="leaf-artwork" role="img" aria-label="Blue leaf artwork with a green lightning bolt">
      <path d="M372,452 Q400,330 500,270 Q600,220 652,140 Q672,330 470,458 Z" fill="url(#leafArea)"/>
    </g>
    <path class="nose-lime" d="M1046,392 Q1100,398 1112,410 L1126,465 L1040,465 Z" fill="var(--lime)"/>
    <path class="headlamp" d="M1062,400 L1108,408 L1113,430 L1068,428 Z" fill="var(--white)"/>
  </g>

  <path class="side-window" d="M800,256 L878,256 L1012,396 L880,389 Q812,382 806,356 Z" fill="var(--page)"/>
  <rect class="door-handle" x="722" y="382" width="38" height="6" rx="3" fill="var(--page)"/>
  <rect class="door-handle" x="788" y="386" width="38" height="6" rx="3" fill="var(--page)"/>

  <text class="headline" x="147" y="185">DORVEL POWER MAX +</text>

  <g class="services">
    <g class="service" transform="translate(174,225)">
      <circle class="service-ring" r="17"/><rect class="service-glyph" x="-9" y="-5" width="18" height="9" rx="1"/>
      <text class="service-label" y="34">Residential</text><text class="service-label" y="50">Service</text>
    </g>
    <g class="service" transform="translate(269,225)">
      <circle class="service-ring" r="17"/><path class="service-glyph" d="M-9,1 L0,-9 L9,1 L9,9 L-9,9 Z"/>
      <text class="service-label" y="34">Commercial</text><text class="service-label" y="50">Service</text>
    </g>
    <g class="service" transform="translate(368,225)">
      <circle class="service-ring" r="17"/><rect class="service-glyph" x="-7" y="-9" width="14" height="18"/>
      <text class="service-label" y="33">New</text><text class="service-label" y="49">Construction</text>
    </g>
    <g class="service" transform="translate(174,305)">
      <circle class="service-ring" r="17"/><path class="service-glyph" d="M-9,1 L0,-9 L9,1 L9,9 L-9,9 Z"/>
      <text class="service-label" y="37">Smart</text><text class="service-label" y="53">Homes</text>
    </g>
    <g class="service" transform="translate(269,305)">
      <circle class="service-ring" r="17"/><rect class="service-glyph" x="-9" y="-7" width="18" height="12"/>
      <text class="service-label" y="37">Solar</text>
    </g>
    <g class="service" transform="translate(368,305)">
      <circle class="service-ring" r="17"/><circle class="service-glyph" cy="-2" r="6"/><rect class="service-glyph" x="-3" y="4" width="6" height="5"/>
      <text class="service-label" y="37">Led</text><text class="service-label" y="53">Lighting</text>
    </g>
  </g>

  <g class="phone-band">
    <path class="phone-pill" d="M92,381 L364,381 Q386,381 386,404 Q386,427 364,427 L92,427 Z"/>
    <circle class="phone-ring" cx="153" cy="404" r="11"/>
    <path d="M148,398 Q147,405 152,410 Q156,413 159,411 L157,408 L154,409 Q151,406 151,402 L153,400 Z" fill="var(--white)"/>
    <text class="phone-text" x="172" y="412">+61-400-555-019</text>
  </g>

  <g class="brand-mark">
    <circle class="brand-dot" cx="826" cy="422" r="14"/>
    <text class="brand-name" x="846" y="429">Dorvel Power+</text>
  </g>

  <polygon class="rocker-strip" points="438,497 908,508 906,525 440,518" fill="var(--charcoal)"/>
</svg>
</body>
</html>
```